Medical supplies company needs a catalogue re-design

Our present catalogue is spread over a number of pages but this needs to be reduced. 4-5 images would require to be on each page. It needs to be professional, simple and elegant. The photos and descriptors need to be adjacent to each other. It should be able to be emailed conventionally as an e-catalogue without it being compressed. an email with existing catalogue will be emailed to anyone interested.
https://www.filevarn.com/s/82kqtb5wzrmuyap/consumables%20photos%20and%20descriptions.pdf?dl=0
Target Market(s)
medical practices, hospitals
Industry/Entity Type
Medical Supply

```html
<!DOCTYPE html>
<html lang="en">
<head>
<meta charset="utf-8">
<title>Medical Supplies Catalogue – Instruments &amp; Gloves</title>
<link href="https://fonts.googleapis.com/css2?family=Arimo:wght@400;700&display=swap" rel="stylesheet">
<style>
:root{
  --canvas:#c9c7c9;
  --page:#ffffff;
  --navy:#23408f;
  --stripe:#7096c2;
  --band-start:#7c9cc6;
  --band-end:#eef2f8;
  --accent:#7196c3;
  --text:#555a60;
  --frame:#6f93c2;
  --photo-a:#eceef2;
  --photo-b:#d7dee8;
}
*{margin:0;padding:0;box-sizing:border-box}
html,body{width:816px;height:1200px;overflow:hidden;background:var(--canvas)}
body{position:relative;font-family:"Arimo",Arial,sans-serif;color:var(--text)}
.page{position:absolute;left:28px;width:758px;height:584px;background:var(--page);
  box-shadow:3px 3px 5px rgba(0,0,0,.35);overflow:hidden}
.page--instruments{top:10px}
.page--gloves{top:606px}
.page-head{position:absolute;left:0;top:0;width:100%;height:60px;
  background:linear-gradient(#e4e8f1,#ffffff)}
.head-stripe{position:absolute;left:0;top:40px;width:100%;height:16px;background:var(--stripe)}
.title-tab{position:absolute;left:248px;top:29px;width:260px;height:48px}
.title-tab svg{position:absolute;inset:0}
.title-tab h1{position:relative;text-align:center;color:#fff;font-size:22px;font-weight:700;line-height:48px;letter-spacing:-.2px}
.page-foot{position:absolute;left:0;bottom:0;width:100%;height:60px;
  background:linear-gradient(#ffffff,#e4e8f1)}
.page-number{position:absolute;left:370px;top:550px;width:19px;height:19px;border-radius:50%;
  background:var(--accent);color:#fff;font-size:11px;font-weight:700;text-align:center;line-height:19px}
.photo{position:absolute;border:2px solid var(--frame);
  background:linear-gradient(135deg,var(--photo-a),var(--photo-b))}
.band{position:absolute;background:linear-gradient(90deg,var(--band-start),var(--band-end));
  color:#fff;font-weight:700;padding-left:11px}
.band--tall{font-size:12.5px;line-height:16px;padding-top:3px}
.band--slim{font-size:12px;line-height:19px;height:19px}
.specs{position:absolute;list-style:none;font-size:10px;line-height:14px}
.specs li::before{content:"•";color:#333;margin-right:3px}
.specs .size{color:var(--accent);font-weight:700}
.specs li.size::before{color:var(--accent)}
</style>
</head>
<body>

<section class="page page--instruments">
  <div class="page-head"></div>
  <div class="head-stripe"></div>
  <div class="title-tab">
    <svg viewBox="0 0 260 48" preserveAspectRatio="none"><polygon points="2,0 258,0 260,10 260,40 130,48 0,40 0,10" fill="#23408f"/></svg>
    <h1>Instruments</h1>
  </div>

  <div class="photo" style="left:34px;top:102px;width:174px;height:171px" role="img" aria-label="Splinter forceps in sterile pouch, front and back"></div>
  <div class="band band--tall" style="left:208px;top:118px;width:176px;height:38px">Splinter Forceps;<br>Hunter</div>
  <ul class="specs" style="left:220px;top:170px">
    <li>Splinter Forceps;<br>&nbsp;&nbsp;Hunter <span class="size">11.5cm</span></li>
    <li>Straight</li><li>Stainless Steel</li><li>Sterile</li>
  </ul>

  <div class="photo" style="left:376px;top:102px;width:174px;height:171px" role="img" aria-label="Fine dressing forceps in sterile pouch, front and back"></div>
  <div class="band band--tall" style="left:550px;top:118px;width:208px;height:38px">Forcep dressing<br>fine</div>
  <ul class="specs" style="left:562px;top:170px">
    <li>Forcep dressing fine <span class="size">12.5cm</span></li>
    <li>Straight</li><li>Stainless Steel</li><li>Sterile</li>
  </ul>

  <div class="photo" style="left:34px;top:310px;width:174px;height:171px" role="img" aria-label="Sharp scissors in sterile pouch, front and back"></div>
  <div class="band band--tall" style="left:208px;top:328px;width:176px;height:38px">Sharp<br>Scissors</div>
  <ul class="specs" style="left:220px;top:380px">
    <li>Sharp Scissors <span class="size">12.5cm</span></li>
    <li>Straight</li><li>Stainless Steel</li><li>Sterile</li>
  </ul>

  <div class="page-foot"></div>
  <div class="page-number">7</div>
</section>

<section class="page page--gloves">
  <div class="page-head"></div>
  <div class="head-stripe"></div>
  <div class="title-tab">
    <svg viewBox="0 0 260 48" preserveAspectRatio="none"><polygon points="2,0 258,0 260,10 260,40 130,48 0,40 0,10" fill="#23408f"/></svg>
    <h1>Gloves</h1>
  </div>

  <div class="photo" style="left:66px;top:77px;width:182px;height:118px" role="img" aria-label="Box of nitrile gloves"></div>
  <div class="band band--slim" style="left:248px;top:93px;width:448px">Nitrile Powder Free and Latex Free Gloves</div>
  <ul class="specs" style="left:263px;top:121px">
    <li>Provides great tactile sensitivity because of normal fingertip thickness</li>
    <li>Powder free</li><li>Latex free</li><li>Ambidextrous</li>
    <li class="size">Small, Medium, Large (box of 100)</li>
  </ul>

  <div class="photo" style="left:66px;top:208px;width:182px;height:118px" role="img" aria-label="Box of latex examination gloves"></div>
  <div class="band band--slim" style="left:248px;top:224px;width:448px">Latex Examination Gloves (non sterile, powder free)</div>
  <ul class="specs" style="left:263px;top:252px">
    <li>Ambidextrous</li><li>Powder free</li><li>Natural Latex with beaded cuff</li><li>Good Grip</li>
    <li class="size">Small, Medium, Large (100 gloves per box)</li>
  </ul>

  <div class="photo" style="left:66px;top:339px;width:182px;height:180px" role="img" aria-label="Box and pack of latex surgical gloves"></div>
  <div class="band band--slim" style="left:248px;top:356px;width:448px">Latex Surgical Gloves without powder</div>
  <ul class="specs" style="left:263px;top:384px">
    <li>Powder free</li><li>Non irritating</li><li>Textured</li><li>Sterile</li>
    <li class="size">6.5, 7, 7.5, 8 (boxes of 50 pairs)</li>
  </ul>
  <div class="band band--slim" style="left:248px;top:454px;width:448px">Sterile Latex Gloves with powder</div>
  <ul class="specs" style="left:263px;top:483px">
    <li>Good grip and feel</li>
    <li>Natural anatomical design reduces thumb and arm stress and results in greater comfort</li>
    <li class="size">7, 7.5, 8 (box of 50 pairs)</li>
  </ul>

  <div class="page-foot"></div>
  <div class="page-number">8</div>
</section>

</body>
</html>
```